Architecture office 10 pages brochure for investors

We need a multi-page brochure (10pg) for our small architectural office.
After the long real estate crisis in Greece we're intend to reborn our architectural planning services, to relocate our targets and to communicate the philosophy in the new era of commercial buildings:
Modern architectural language, Highly energy efficient buildings with green and passive oriented design and functional details. Multifamily housing, Office buildings, Hotels, Refurbishment and Interiors from a group of new architects collaborators and an experienced leader.
We need fresh, clever styling with minimal expression and reach meanings. Written in two languages (ENG-GR) the fonts must be compatible. The solution of an digital and non-printed brochure, for on-line sharing, its a possibility and maybe unlock animated and / or AR solutions. The green color -as attached- will be appreciated.

Please provide your professional opinion about the set up of the pages.
An idea given: minimal frontpage, 2-3nd pages "about us" and "contents with photo and some minor text, and every next page refers one selected project with photo and some text for two languages (4-7 pages projects), pages 8-9 listed works-projects, collaborators, clients.
Updates

low design entries -one entry as 4 projects- , low quality, not satisfying the wills

Target Market(s)

investors in commercial buildings, private clients, energy efficiency

Industry/Entity Type

Architecture

Font styles to use
Sans Serif
Other font styles liked:
• greek compatible

Requirements
Must have
• clear - minimal design, photos, illustrations, text, contents.
• some of the projects can find them in attached link,
Nice to have
• dynamic lines, hand drawing sketches
• maybe the building design process: thoughts, sketch, hand design, cad, collaboration with other engineers, 3d renderings, animations ....
Should not have
• art deco, romantic styles, full red or basic contrasting colors (red/green, purple/orange etc)

```html
<!DOCTYPE html>
<html lang="en">
<head>
<meta charset="UTF-8">
<title>About Us – Brochure Spread</title>
<link rel="stylesheet" href="https://fonts.googleapis.com/css2?family=Montserrat:wght@300;400;500;600;700&display=swap">
<style>
  :root {
    --backdrop: #454545;
    --paper: #f7f7f6;
    --paper-right: #fbfbfa;
    --ink: #2e2e2e;
    --ink-soft: #5a5a5a;
    --quote: #b9b9b9;
    --accent: #b7c93c;
    --accent-soft: #cbd86e;
    --sky: #5d8fe0;
    --facade: #c9c1ad;
  }
  * { box-sizing: border-box; margin: 0; padding: 0; }
  html, body {
    width: 1200px; height: 900px; overflow: hidden;
    background: var(--backdrop);
    font-family: "Montserrat", sans-serif;
    color: var(--ink);
  }
  .spread {
    position: absolute; left: 120px; top: 110px;
    width: 960px; height: 680px;
    box-shadow: 0 18px 40px rgba(0,0,0,.35);
  }
  .page {
    position: absolute; top: 0; width: 480px; height: 680px;
  }
  .page--left { left: 0; background: var(--paper); }
  .page--right { left: 480px; background: var(--paper-right); }
  .spine {
    position: absolute; left: 460px; top: 0; width: 40px; height: 680px;
    background: linear-gradient(90deg, rgba(0,0,0,0) 0%, rgba(0,0,0,.07) 50%, rgba(0,0,0,0) 100%);
    pointer-events: none; z-index: 3;
  }
  .hero-photo {
    position: absolute; left: 190px; top: 40px; width: 530px; height: 270px;
    background:
      linear-gradient(160deg, transparent 45%, rgba(150,150,140,.55) 78%, #a9a9a3 100%),
      linear-gradient(180deg, var(--sky) 0%, #8fb3ea 30%, var(--facade) 55%, #b8b8ad 78%, #8e9a7a 100%);
    z-index: 2;
  }

  /* Left page */
  .about-title {
    position: absolute; left: 40px; top: 240px;
    font-size: 26px; font-weight: 300; letter-spacing: 1px; color: var(--ink);
  }
  .about-title strong { font-weight: 700; color: var(--accent); }
  .about-title::before {
    content: ""; position: absolute; left: 0; top: -8px; width: 18px; height: 2px; background: var(--accent);
  }
  .about-body {
    position: absolute; left: 40px; top: 322px; width: 400px;
    font-size: 9.5px; line-height: 1.55; color: var(--ink-soft);
  }
  .about-body p + p { margin-top: 12px; }

  .page-footer { position: absolute; left: 40px; right: 40px; bottom: 36px; height: 40px; }
  .page-footer__url {
    position: absolute; left: 0; top: 0; font-size: 8px; font-weight: 600; color: var(--ink);
  }
  .page-footer__rule {
    position: absolute; left: 0; right: 16px; top: 22px; height: 1px; background: var(--accent-soft);
  }
  .page-footer__num {
    position: absolute; right: 0; top: 14px; width: 16px; height: 16px; border-radius: 50%;
    background: var(--accent); color: #fff; font-size: 7px; font-weight: 600;
    display: flex; align-items: center; justify-content: center;
  }

  /* Right page */
  .feature-rule {
    position: absolute; left: 256px; top: 118px; width: 1px; height: 86px; background: var(--accent);
  }
  .feature-title {
    position: absolute; left: 268px; top: 118px; width: 190px;
    font-size: 16px; line-height: 1.2; font-weight: 600; color: var(--accent); text-transform: uppercase;
  }
  .feature-body {
    position: absolute; left: 268px; top: 214px; width: 190px;
    font-size: 7.5px; line-height: 1.5; color: var(--ink-soft);
  }
  .feature-body p + p { margin-top: 8px; }

  .pull-quote {
    position: absolute; left: 40px; top: 345px; width: 170px;
    font-size: 16px; font-weight: 300; line-height: 1.4; color: var(--quote);
  }
  .pull-quote__mark {
    display: block; font-size: 32px; font-weight: 700; line-height: 1; color: #c7c7c7;
  }
  .pull-quote__mark--close { text-align: center; margin-top: 4px; }

  .steps { position: absolute; left: 232px; top: 412px; width: 226px; }
  .steps__title { font-size: 10px; font-weight: 600; line-height: 1.3; color: var(--ink); margin-bottom: 10px; }
  .steps__list { list-style: none; }
  .step { display: flex; gap: 10px; margin-bottom: 10px; }
  .step__num {
    flex: none; width: 15px; height: 15px; background: var(--accent); color: #fff;
    font-size: 8px; font-weight: 600; display: flex; align-items: center; justify-content: center;
  }
  .step__text { font-size: 7.5px; line-height: 1.5; color: var(--ink-soft); }
</style>
</head>
<body>
  <main class="spread">
    <section class="page page--left">
      <h1 class="about-title">ABOUT <strong>US</strong></h1>
      <div class="about-body">
        <p>Lorem ipsum dolor sit amet, consectetur adipiscing elit, sed do eiusmod tempor incididunt ut labore et dolore magna aliqua. Ut enim ad minim veniam, quis nostrud exercitation ullamco laboris nisi ut aliquip ex ea commodo consequat. Duis aute irure dolor in reprehenderit in voluptate velit esse cillum dolore eu fugiat nulla pariatur. Excepteur sint occaecat cupidatat non proident, sunt in culpa qui officia deserunt mollit anim id est laborum.</p>
        <p>Sed ut perspiciatis unde omnis iste natus error sit voluptatem accusantium doloremque laudantium, totam rem aperiam, eaque ipsa quae ab illo inventore veritatis et quasi architecto beatae vitae dicta sunt explicabo. Nemo enim ipsam voluptatem quia voluptas sit aspernatur aut odit aut fugit, sed quia consequuntur magni dolores eos qui ratione voluptatem sequi nesciunt.</p>
      </div>
      <footer class="page-footer">
        <span class="page-footer__url">www.lineahaus-studio.com</span>
        <span class="page-footer__rule"></span>
        <span class="page-footer__num">01</span>
      </footer>
    </section>

    <section class="page page--right">
      <span class="feature-rule"></span>
      <h2 class="feature-title">Lorem ipsum dolor sit amet, consectetur adipiscing elit</h2>
      <div class="feature-body">
        <p>Lorem ipsum dolor sit amet, consectetur adipiscing elit, sed do eiusmod tempor incididunt ut labore et dolore magna aliqua. Ut enim ad minim veniam, quis nostrud exercitation ullamco laboris nisi ut aliquip ex ea commodo consequat. Duis aute irure dolor in reprehenderit in voluptate velit esse cillum dolore eu fugiat nulla pariatur.</p>
        <p>Sed ut perspiciatis unde omnis iste natus error sit voluptatem accusantium doloremque laudantium, totam rem aperiam, eaque ipsa quae ab illo inventore veritatis et quasi architecto beatae vitae dicta sunt explicabo. Nemo enim ipsam voluptatem quia voluptas sit aspernatur.</p>
      </div>

      <blockquote class="pull-quote">
        <span class="pull-quote__mark">&ldquo;</span>
        consectetur adipiscing elit, sed do eiusmod tempor incididunt ut labore et dolore magna aliqua
        <span class="pull-quote__mark pull-quote__mark--close">&rdquo;</span>
      </blockquote>

      <div class="steps">
        <h3 class="steps__title">Lorem ipsum dolor<br>sit amet, consectetur adipiscing elit</h3>
        <ol class="steps__list">
          <li class="step"><span class="step__num">1</span><span class="step__text">sed do eiusmod tempor incididunt ut labore et dolore magna aliqua. Ut enim ad minim veniam, ut aliquip ex ea commodo consequat.</span></li>
          <li class="step"><span class="step__num">2</span><span class="step__text">sed do eiusmod tempor incididunt ut labore et dolore magna aliqua. Ut enim ad minim veniam, ut aliquip ex ea commodo consequat.</span></li>
          <li class="step"><span class="step__num">3</span><span class="step__text">sed do eiusmod tempor incididunt ut labore et dolore magna aliqua. Ut enim ad minim veniam, ut aliquip ex ea commodo consequat.</span></li>
        </ol>
      </div>

      <footer class="page-footer">
        <span class="page-footer__url">www.lineahaus-studio.com</span>
        <span class="page-footer__rule"></span>
        <span class="page-footer__num">02</span>
      </footer>
    </section>

    <div class="hero-photo" role="img" aria-label="Photograph of a modern white multi-storey residential building with glass balconies and timber cladding under a blue sky, trees in front"></div>
    <div class="spine"></div>
  </main>
</body>
</html>
```